Create a "germ free" Poster Design Project

Hi we're a media business who sells advertising space on a unique dispensing device that also sanitizes your hands.

I'm looking for a poster design that highlights the need to sanitize hands which removes 99.9% of germs and also promotes a healthy & clean lifestyle.
(you may want to use kid friendly images of bugs to highlight germs)
Whilst the primary message will be to sanitize your hands the secondary message is also to "use this space" to advertise on.

The poster should be colorful yet simple and not too wordy.

Thanks

Target Market(s)

General cunsumer public but more specifically women and moms

Industry/Entity Type

Advertising

Requirements
Must have
• A central picture (animated or real) to highlight the practice of sanitizing hands (or removing germs)
Perhaps an arrow down to invite consumers to "try it now, its free'
Nice to have
• Referal to our web site: Brelvona.com.au (currently not operational) and email info@brelvona.com.au
Perhaps an image of a baby's hand with a creative tag line.
Should not have
• Nothing too gross looking

```html
<!DOCTYPE html>
<html lang="en">
<head>
<meta charset="utf-8">
<title>Sanitising Hands Posters</title>
<link rel="stylesheet" href="https://fonts.googleapis.com/css2?family=Exo+2:wght@700;800&family=Roboto+Condensed:wght@700&family=Arimo:wght@700&display=swap">
<style>
  :root {
    --stage: #0f57a8;
    --navy: #1f4774;
    --cta-red: #d8261c;
    --brand-magenta: #c8177a;
    --ink: #111111;
    --paper: #ffffff;
    --peach: #f3a98c;
    --cyan: #2fb6e4;
  }
  * { margin: 0; padding: 0; box-sizing: border-box; }
  html, body {
    width: 1149px;
    height: 1200px;
    overflow: hidden;
    background: var(--stage);
  }
  .poster {
    position: absolute;
    top: 11px;
    width: 379px;
    height: 1111px;
    background: var(--paper);
    overflow: hidden;
  }
  .poster--girl { left: 129px; }
  .poster--boy { left: 632px; }
  .poster__art {
    position: absolute;
    inset: 0;
    width: 379px;
    height: 1111px;
  }
  .band__text {
    font-family: "Exo 2", sans-serif;
    font-weight: 700;
    font-size: 16px;
    fill: #ffffff;
  }
  .poster__kicker {
    position: absolute;
    top: 51px;
    left: 0;
    width: 100%;
    text-align: center;
    font-family: "Roboto Condensed", sans-serif;
    font-weight: 700;
    font-size: 22px;
    color: var(--navy);
    letter-spacing: -0.2px;
  }
  .poster__headline {
    position: absolute;
    top: 128px;
    left: 0;
    width: 100%;
    text-align: center;
    font-family: "Exo 2", sans-serif;
    font-weight: 800;
    font-size: 47px;
    line-height: 49.5px;
    color: var(--navy);
    letter-spacing: -0.5px;
  }
  .poster__cta {
    position: absolute;
    top: 738px;
    left: 0;
    width: 100%;
    display: flex;
    justify-content: center;
    align-items: center;
    gap: 7px;
    font-family: "Arimo", sans-serif;
    font-weight: 700;
    font-size: 25px;
    letter-spacing: -0.6px;
    color: var(--cta-red);
  }
  .poster__cta svg { width: 34px; height: 34px; flex: none; }
  .poster__brand {
    position: absolute;
    top: 910px;
    left: 0;
    width: 100%;
    display: flex;
    justify-content: center;
    align-items: center;
    gap: 14px;
  }
  .brand__dot {
    width: 58px;
    height: 58px;
    border-radius: 50%;
    background: var(--brand-magenta);
  }
  .brand__name {
    font-family: "Exo 2", sans-serif;
    font-weight: 700;
    font-size: 42px;
    color: var(--brand-magenta);
  }
  .poster__contact {
    position: absolute;
    top: 1026px;
    left: 0;
    width: 100%;
    text-align: center;
    font-family: "Arimo", sans-serif;
    font-weight: 700;
    font-size: 20px;
    line-height: 27px;
    color: var(--ink);
  }
  .contact__label { color: var(--cta-red); }
  .contact__email { text-decoration: underline; }
</style>
</head>
<body>

<section class="poster poster--girl">
  <svg class="poster__art" viewBox="0 0 379 1111" xmlns="http://www.w3.org/2000/svg">
    <defs>
      <linearGradient id="girl-sky" x1="0" y1="0" x2="0" y2="1">
        <stop offset="0" stop-color="#f4ecaa"/>
        <stop offset="0.18" stop-color="#f1dcb4"/>
        <stop offset="0.42" stop-color="#ecc9c4"/>
        <stop offset="0.6" stop-color="#f4dedd"/>
        <stop offset="0.68" stop-color="#ffffff"/>
      </linearGradient>
      <linearGradient id="girl-photo" x1="0" y1="0" x2="1" y2="1">
        <stop offset="0" stop-color="#3aa6d8"/>
        <stop offset="0.45" stop-color="#9fc6e0"/>
        <stop offset="0.7" stop-color="#d9a98e"/>
        <stop offset="1" stop-color="#e8d6c8"/>
      </linearGradient>
      <linearGradient id="girl-band" x1="0" y1="0" x2="1" y2="0">
        <stop offset="0" stop-color="#a24aa8"/>
        <stop offset="0.6" stop-color="#7a2c8c"/>
        <stop offset="1" stop-color="#5e2a86"/>
      </linearGradient>
      <radialGradient id="girl-glow">
        <stop offset="0" stop-color="#ffffff"/>
        <stop offset="1" stop-color="#ffffff" stop-opacity="0"/>
      </radialGradient>
    </defs>
    <rect width="379" height="1111" fill="url(#girl-sky)"/>
    <path d="M30 0 C 60 120 200 170 379 160 L379 0 Z" fill="#f6f0b8" opacity="0.7"/>
    <path d="M0 150 C 120 240 260 260 379 300 L379 360 C 250 320 100 300 0 260 Z" fill="#ffffff" opacity="0.18"/>
    <ellipse cx="172" cy="422" rx="20" ry="12" fill="url(#girl-glow)"/>
    <path d="M0 545 C 30 515 70 492 110 488 L90 560 Z" fill="var(--cyan)"/>
    <path d="M170 490 C 250 460 330 468 379 500 L379 600 L200 520 Z" fill="var(--peach)"/>
    <path class="art__photo" role="img" aria-label="Photo of a smiling girl with pigtails giving a thumbs up while drying her hands"
          d="M0 548 C 40 505 80 482 140 478 C 220 472 310 468 379 500 L379 600 C 365 650 340 700 290 680 C 200 640 100 530 0 548 Z"
          fill="url(#girl-photo)"/>
    <path d="M0 598 C 100 580 200 690 290 727 C 340 745 365 700 379 650 L379 720 C 340 790 250 760 160 700 C 90 660 40 640 0 640 Z" fill="#f1e3ee" opacity="0.8"/>
    <path d="M0 548 C 100 530 200 640 290 680 C 340 700 365 650 379 600 L379 650 C 365 700 340 745 290 727 C 200 690 100 580 0 598 Z" fill="url(#girl-band)"/>
    <path id="girl-band-line" d="M14 574 C 110 565 205 672 292 706 C 330 720 355 700 374 664" fill="none"/>
    <text class="band__text">
      <textPath href="#girl-band-line" startOffset="2%">Promotes a healthy &amp; clean lifestyle.</textPath>
    </text>
  </svg>

  <p class="poster__kicker">USE THIS SPACE</p>
  <h1 class="poster__headline">Sanitising<br>hands<br>removes<br>99.9% of<br>germs</h1>
  <p class="poster__cta">
    <svg viewBox="0 0 34 34" aria-hidden="true"><circle cx="17" cy="17" r="14.5" fill="none" stroke="var(--cta-red)" stroke-width="2.5"/><path d="M17 8 V24 M11 18 L17 25 L23 18" fill="none" stroke="var(--cta-red)" stroke-width="2.8" stroke-linecap="round" stroke-linejoin="round"/></svg>
    <span>TRY IT NOW, ITS FREE</span>
  </p>
  <div class="poster__brand">
    <span class="brand__dot"></span>
    <span class="brand__name">Brelvona</span>
  </div>
  <p class="poster__contact">
    <span class="contact__web">www.brelvona.com.au</span><br>
    <span class="contact__label">email</span> <span class="contact__email">info@brelvona.com.au</span>
  </p>
</section>

<section class="poster poster--boy">
  <svg class="poster__art" viewBox="0 0 379 1111" xmlns="http://www.w3.org/2000/svg">
    <defs>
      <linearGradient id="boy-sky" x1="0" y1="0" x2="0" y2="1">
        <stop offset="0" stop-color="#f4ecaa"/>
        <stop offset="0.18" stop-color="#f1dcb4"/>
        <stop offset="0.42" stop-color="#ecc9c4"/>
        <stop offset="0.6" stop-color="#f4dedd"/>
        <stop offset="0.68" stop-color="#ffffff"/>
      </linearGradient>
      <linearGradient id="boy-photo" x1="0" y1="0" x2="1" y2="1">
        <stop offset="0" stop-color="#1f9a9a"/>
        <stop offset="0.45" stop-color="#2e9f9c"/>
        <stop offset="0.6" stop-color="#e3b39a"/>
        <stop offset="1" stop-color="#9fb6d4"/>
      </linearGradient>
      <linearGradient id="boy-band" x1="0" y1="0" x2="1" y2="0">
        <stop offset="0" stop-color="#a24aa8"/>
        <stop offset="0.6" stop-color="#7a2c8c"/>
        <stop offset="1" stop-color="#5e2a86"/>
      </linearGradient>
      <radialGradient id="boy-glow">
        <stop offset="0" stop-color="#ffffff"/>
        <stop offset="1" stop-color="#ffffff" stop-opacity="0"/>
      </radialGradient>
    </defs>
    <rect width="379" height="1111" fill="url(#boy-sky)"/>
    <path d="M30 0 C 60 120 200 170 379 160 L379 0 Z" fill="#f6f0b8" opacity="0.7"/>
    <path d="M0 150 C 120 240 260 260 379 300 L379 360 C 250 320 100 300 0 260 Z" fill="#ffffff" opacity="0.18"/>
    <ellipse cx="172" cy="422" rx="20" ry="12" fill="url(#boy-glow)"/>
    <path d="M170 490 C 250 460 330 468 379 500 L379 600 L200 520 Z" fill="var(--peach)"/>
    <path class="art__photo" role="img" aria-label="Photo of a young boy in a blue shirt holding up both open hands"
          d="M0 548 C 40 505 80 482 140 478 C 220 472 310 468 379 500 L379 600 C 365 650 340 700 290 680 C 200 640 100 530 0 548 Z"
          fill="url(#boy-photo)"/>
    <path d="M0 598 C 100 580 200 690 290 727 C 340 745 365 700 379 650 L379 720 C 340 790 250 760 160 700 C 90 660 40 640 0 640 Z" fill="#f1e3ee" opacity="0.8"/>
    <path d="M0 548 C 100 530 200 640 290 680 C 340 700 365 650 379 600 L379 650 C 365 700 340 745 290 727 C 200 690 100 580 0 598 Z" fill="url(#boy-band)"/>
    <path id="boy-band-line" d="M14 574 C 110 565 205 672 292 706 C 330 720 355 700 374 664" fill="none"/>
    <text class="band__text">
      <textPath href="#boy-band-line" startOffset="2%">Promotes a healthy &amp; clean lifestyle.</textPath>
    </text>
  </svg>

  <p class="poster__kicker">USE THIS SPACE</p>
  <h2 class="poster__headline">Sanitising<br>hands<br>removes<br>99.9% of<br>germs</h2>
  <p class="poster__cta">
    <svg viewBox="0 0 34 34" aria-hidden="true"><circle cx="17" cy="17" r="14.5" fill="none" stroke="var(--cta-red)" stroke-width="2.5"/><path d="M17 8 V24 M11 18 L17 25 L23 18" fill="none" stroke="var(--cta-red)" stroke-width="2.8" stroke-linecap="round" stroke-linejoin="round"/></svg>
    <span>TRY IT NOW, ITS FREE</span>
  </p>
  <div class="poster__brand">
    <span class="brand__dot"></span>
    <span class="brand__name">Brelvona</span>
  </div>
  <p class="poster__contact">
    <span class="contact__web">www.brelvona.com.au</span><br>
    <span class="contact__label">email</span> <span class="contact__email">info@brelvona.com.au</span>
  </p>
</section>

</body>
</html>
```